Global Beard Oil Review Business needs a refresh

topwhiskertonic.net is a global business who's mission is to curate all available beard oils from around the world, review and grade them and present this curated collection to the user of the website.

The scope of this job includes the web site design and the design of a suitable logo to be used in the site header.

The existing site can be seen on http://topwhiskertonic.net, however this is a mock-up only the style and logo should NOT be used. This is to give you an idea of the concept of the site only.

This job is for PSD design only.

See attached design brief for detailed design requirements.
Updates

Project Deadline Extended
Reason: Extending deadline by 5 days to allow for final submissions

Target Market(s)

Men's grooming / retail

Industry/Entity Type

Retail

Number of Pages Required

2 page

Font styles to use
Sans Serif

Requirements
Must have
• 1) Comparison Table
• 2) Side Bar
• 3) Header area
• 4) Photo of Calvin Dorrow (attached - can be circular or "cut-out")
• 5) Cool beard-oriented custom design background (e.g., stylistic black/brown on brown/orange beard background. I envision this beard background "drawing" rather than photo based)
• (see attached design requirements for details)
Nice to have
• Signature style writing at top with name "Calvin Dorrow"
Should not have
• Do NOT use the look & feel or logo from the existing site.

```html
<!DOCTYPE html>
<html lang="en">
<head>
<meta charset="utf-8">
<title>Top Whisker Tonic — Beard Oil Reviews</title>
<link href="https://fonts.googleapis.com/css2?family=Roboto:wght@300;400;500;700&display=swap" rel="stylesheet">
<style>
:root{
  --page:#f8f4f0;
  --brand-red:#a5200f;
  --orange:#f39a3c;
  --orange-text:#d2691e;
  --brown:#6b4a36;
  --brown-dark:#2c1f19;
  --row-alt:#efebe8;
  --line:#e2dcd7;
  --text:#4a4a4a;
  --muted:#8a8a8a;
}
*{box-sizing:border-box;margin:0;padding:0}
html,body{width:938px;height:1200px;overflow:hidden}
body{background:var(--page);font-family:"Roboto",Arial,sans-serif;color:var(--text);position:relative}

/* Header */
.site-header{position:absolute;left:92px;top:0;width:751px;height:78px}
.brand{position:absolute;left:2px;top:19px;width:212px;white-space:nowrap}
.brand-name{font-size:22px;font-weight:700;color:var(--brand-red);line-height:1}
.brand-tagline{font-size:12px;color:var(--text);text-align:right;margin-top:4px}
.portrait{position:absolute;left:222px;top:9px;width:54px;height:54px;border-radius:50%;background:radial-gradient(circle at 50% 40%,#8a9a8f,#4c5a55);border:3px solid #e8e2dc}
.call{position:absolute;right:0;top:16px;display:flex;align-items:center;gap:5px;text-align:right}
.call small{display:block;font-size:7.5px;color:var(--muted)}
.call strong{display:block;font-size:12px;font-weight:500;color:var(--orange)}
.call-icon{width:21px;height:21px;border-radius:50%;background:var(--orange);display:flex;align-items:center;justify-content:center}
.main-nav{position:absolute;right:0;top:53px;display:flex;gap:18px;font-size:7.5px}
.main-nav a{color:var(--text);text-decoration:none}
.main-nav a.active{color:var(--brand-red)}

/* Hero */
.hero{position:absolute;left:92px;top:78px;width:751px;height:260px;background:repeating-linear-gradient(180deg,#e4e3e1 0 58px,#c9c8c6 58px 60px),#e4e3e1}
.hero h1{position:absolute;left:62px;top:114px;font-weight:300;font-size:23px;line-height:26px;color:#4b4b4b}
.hero-person{position:absolute;left:430px;top:0;width:300px;height:260px;background:radial-gradient(ellipse at 40% 20%,#7a4a30 0 18%,transparent 30%),linear-gradient(180deg,transparent 40%,#3f5f82 55%,#2f4a6a);border-radius:40% 40% 0 0}
.slider-dots{position:absolute;left:351px;top:312px;width:50px;height:12px;border-radius:6px;background:#9a9a9a;display:flex;justify-content:center;align-items:center;gap:4px}
.slider-dots i{width:5px;height:5px;border-radius:50%;background:#fff}
.slider-dots i:first-child{background:transparent;border:1px solid #fff}

/* Comparison table */
.compare{position:absolute;left:93px;top:358px;width:583px}
.row{display:grid;grid-template-columns:63px 65px 56px 60px 66px 59px 34px 55px 30px 33px 62px;height:38px;font-size:7.5px;background:#fff}
.row:nth-child(odd){background:var(--row-alt)}
.row>span{display:flex;align-items:center;justify-content:center;text-align:center;border-right:1px solid var(--line);line-height:9px}
.row>span:last-child{border-right:0}
.row.head{height:31px;background:var(--brown);color:#fff;font-size:8px}
.row.head>span{border-color:#5a3c2b}
.row .supplier{justify-content:flex-start;padding-left:11px;text-align:left;color:var(--orange-text)}
.row .name{color:var(--orange-text)}
.bottle{width:10px;height:26px;border-radius:3px 3px 2px 2px;background:linear-gradient(180deg,#b58560 0 20%,#d49a5f 20%,#b06f36)}
.score{flex-direction:column;gap:6px}
.bar{display:block;width:24px;height:2px;background:#c8c2bd;position:relative}
.bar::before{content:"";position:absolute;left:0;top:0;height:2px;width:65%;background:var(--orange-text)}
.dots{display:block;width:24px;height:4px;background:radial-gradient(circle,#b5b0ac 1.6px,transparent 2px) 0 0/5px 4px repeat-x;position:relative}
.dots::before{content:"";position:absolute;left:0;top:0;width:20px;height:4px;background:radial-gradient(circle,var(--orange-text) 1.6px,transparent 2px) 0 0/5px 4px repeat-x}
.buy{gap:4px;color:#222}
.buy svg{width:8px;height:8px}
.buy.primary span{background:var(--orange);color:#fff;padding:5px 7px;border-radius:2px;display:flex;gap:4px;align-items:center}

/* Sidebar */
.sidebar{position:absolute;left:686px;top:356px;width:157px}
.sidebar h2{font-size:12px;font-weight:400;color:var(--brand-red)}
.subscribe{margin-top:3px;height:25px;background:var(--brown);color:#fff;font-size:6px;display:flex;align-items:center;justify-content:space-between;padding:0 9px 0 10px}
.social{display:flex;gap:5px;margin-top:16px}
.social i{width:16px;height:16px;border-radius:50%;background:var(--brown)}
.blog-title{margin-top:16px;height:30px;background:var(--brand-red);color:#fff;font-size:13px;padding:7px 12px}
.post{display:flex;gap:7px;margin-top:5px;height:57px;background:#f2efec;border:1px solid var(--line);padding:5px}
.post+.post{margin-top:5px}
.thumb{flex:none;width:40px;height:45px}
.post p{font-size:6.6px;line-height:9px;text-align:justify}
.post time{display:block;font-size:6.2px;margin-top:3px}

/* Footer */
.site-footer{position:absolute;left:92px;top:1132px;width:751px;height:68px;background:var(--brown-dark);color:#b9b0a9;font-size:7px;text-align:center;padding-top:20px}
.site-footer nav{display:flex;justify-content:center;gap:6px}
.site-footer p{margin-top:11px}
</style>
</head>
<body>
<svg width="0" height="0" style="position:absolute">
  <symbol id="cart" viewBox="0 0 10 10"><path d="M0 1h2l1.2 5h5L9.6 2.5H3" fill="none" stroke="currentColor" stroke-width="1.3"/><circle cx="3.8" cy="8.5" r="1" fill="currentColor"/><circle cx="7.6" cy="8.5" r="1" fill="currentColor"/></symbol>
</svg>

<header class="site-header">
  <div class="brand">
    <div class="brand-name">Top Whisker Tonic</div>
    <div class="brand-tagline">with Calvin Dorrow</div>
  </div>
  <div class="portrait" role="img" aria-label="Portrait photo of Calvin Dorrow"></div>
  <div class="call">
    <div><small>Call us on</small><strong>555 014 2290</strong></div>
    <div class="call-icon"><svg width="10" height="10" viewBox="0 0 10 10"><path d="M2 1l2 2-1 1.2c.6 1.2 1.6 2.2 2.8 2.8L7 6l2 2-1.3 1.3C4.5 9 1 5.5.7 2.3z" fill="#fff"/></svg></div>
  </div>
  <nav class="main-nav">
    <a class="active" href="#">Home</a><a href="#">About Me</a><a href="#">Beard Oil Review Methodology</a><a href="#">Charter</a><a href="#">Blog</a>
  </nav>
</header>

<section class="hero">
  <div class="hero-person" role="img" aria-label="Photo of a bearded man in sunglasses and a denim shirt against a white wood wall"></div>
  <h1>The World’s #1<br>Beard Oil Authority</h1>
  <div class="slider-dots"><i></i><i></i><i></i><i></i></div>
</section>

<main class="compare">
  <div class="row head"><span>Supplier</span><span>Name</span><span>Photo</span><span>Origin</span><span>Base Oil</span><span>Scent</span><span>Aroma</span><span>Therapeutic<br>Affect</span><span>Value</span><span>Overall</span><span></span></div>

  <div class="row"><span class="supplier">Bristle<br>Barrel</span><span class="name">Timberline</span><span><i class="bottle" role="img" aria-label="Beard oil bottle"></i></span><span>USA</span><span>Curabitur turpis</span><span>Suspendisse<br>placerat</span><span class="score">6<b class="bar"></b></span><span class="score">3<b class="dots"></b></span><span class="score">7<b class="bar"></b></span><span class="score">7<b class="bar"></b></span><span class="buy primary"><span><svg><use href="#cart"/></svg>Buy Now</span></span></div>
  <div class="row"><span class="supplier">Bristle<br>Barrel</span><span class="name">Timberline</span><span><i class="bottle" role="img" aria-label="Beard oil bottle"></i></span><span>USA</span><span>Curabitur turpis</span><span>Cras mattis</span><span class="score">6<b class="bar"></b></span><span class="score">3<b class="dots"></b></span><span class="score">5<b class="bar"></b></span><span class="score">9<b class="bar"></b></span><span class="buy"><svg><use href="#cart"/></svg>Buy Now</span></div>
  <div class="row"><span class="supplier">Bristle<br>Barrel</span><span class="name">Timberline</span><span><i class="bottle" role="img" aria-label="Beard oil bottle"></i></span><span>USA</span><span>Curabitur turpis</span><span>Suspendisse<br>placerat</span><span class="score">6<b class="bar"></b></span><span class="score">3<b class="dots"></b></span><span class="score">7<b class="bar"></b></span><span class="score">7<b class="bar"></b></span><span class="buy"><svg><use href="#cart"/></svg>Buy Now</span></div>
  <div class="row"><span class="supplier">Bristle<br>Barrel</span><span class="name">Timberline</span><span><i class="bottle" role="img" aria-label="Beard oil bottle"></i></span><span>USA</span><span>Curabitur turpis</span><span>Cras mattis</span><span class="score">6<b class="bar"></b></span><span class="score">3<b class="dots"></b></span><span class="score">5<b class="bar"></b></span><span class="score">9<b class="bar"></b></span><span class="buy"><svg><use href="#cart"/></svg>Buy Now</span></div>
  <div class="row"><span class="supplier">Bristle<br>Barrel</span><span class="name">Timberline</span><span><i class="bottle" role="img" aria-label="Beard oil bottle"></i></span><span>USA</span><span>Curabitur turpis</span><span>Suspendisse<br>placerat</span><span class="score">6<b class="bar"></b></span><span class="score">3<b class="dots"></b></span><span class="score">7<b class="bar"></b></span><span class="score">7<b class="bar"></b></span><span class="buy"><svg><use href="#cart"/></svg>Buy Now</span></div>
  <div class="row"><span class="supplier">Bristle<br>Barrel</span><span class="name">Timberline</span><span><i class="bottle" role="img" aria-label="Beard oil bottle"></i></span><span>USA</span><span>Curabitur turpis</span><span>Cras mattis</span><span class="score">6<b class="bar"></b></span><span class="score">3<b class="dots"></b></span><span class="score">5<b class="bar"></b></span><span class="score">9<b class="bar"></b></span><span class="buy"><svg><use href="#cart"/></svg>Buy Now</span></div>
  <div class="row"><span class="supplier">Bristle<br>Barrel</span><span class="name">Timberline</span><span><i class="bottle" role="img" aria-label="Beard oil bottle"></i></span><span>USA</span><span>Curabitur turpis</span><span>Suspendisse<br>placerat</span><span class="score">6<b class="bar"></b></span><span class="score">3<b class="dots"></b></span><span class="score">7<b class="bar"></b></span><span class="score">7<b class="bar"></b></span><span class="buy"><svg><use href="#cart"/></svg>Buy Now</span></div>
  <div class="row"><span class="supplier">Bristle<br>Barrel</span><span class="name">Timberline</span><span><i class="bottle" role="img" aria-label="Beard oil bottle"></i></span><span>USA</span><span>Curabitur turpis</span><span>Cras mattis</span><span class="score">6<b class="bar"></b></span><span class="score">3<b class="dots"></b></span><span class="score">5<b class="bar"></b></span><span class="score">9<b class="bar"></b></span><span class="buy"><svg><use href="#cart"/></svg>Buy Now</span></div>
  <div class="row"><span class="supplier">Bristle<br>Barrel</span><span class="name">Timberline</span><span><i class="bottle" role="img" aria-label="Beard oil bottle"></i></span><span>USA</span><span>Curabitur turpis</span><span>Suspendisse<br>placerat</span><span class="score">6<b class="bar"></b></span><span class="score">3<b class="dots"></b></span><span class="score">7<b class="bar"></b></span><span class="score">7<b class="bar"></b></span><span class="buy"><svg><use href="#cart"/></svg>Buy Now</span></div>
  <div class="row"><span class="supplier">Bristle<br>Barrel</span><span class="name">Timberline</span><span><i class="bottle" role="img" aria-label="Beard oil bottle"></i></span><span>USA</span><span>Curabitur turpis</span><span>Cras mattis</span><span class="score">6<b class="bar"></b></span><span class="score">3<b class="dots"></b></span><span class="score">5<b class="bar"></b></span><span class="score">9<b class="bar"></b></span><span class="buy"><svg><use href="#cart"/></svg>Buy Now</span></div>
  <div class="row"><span class="supplier">Bristle<br>Barrel</span><span class="name">Timberline</span><span><i class="bottle" role="img" aria-label="Beard oil bottle"></i></span><span>USA</span><span>Curabitur turpis</span><span>Suspendisse<br>placerat</span><span class="score">6<b class="bar"></b></span><span class="score">3<b class="dots"></b></span><span class="score">7<b class="bar"></b></span><span class="score">7<b class="bar"></b></span><span class="buy"><svg><use href="#cart"/></svg>Buy Now</span></div>
  <div class="row"><span class="supplier">Bristle<br>Barrel</span><span class="name">Timberline</span><span><i class="bottle" role="img" aria-label="Beard oil bottle"></i></span><span>USA</span><span>Curabitur turpis</span><span>Cras mattis</span><span class="score">6<b class="bar"></b></span><span class="score">3<b class="dots"></b></span><span class="score">5<b class="bar"></b></span><span class="score">9<b class="bar"></b></span><span class="buy"><svg><use href="#cart"/></svg>Buy Now</span></div>
  <div class="row"><span class="supplier">Bristle<br>Barrel</span><span class="name">Timberline</span><span><i class="bottle" role="img" aria-label="Beard oil bottle"></i></span><span>USA</span><span>Curabitur turpis</span><span>Suspendisse<br>placerat</span><span class="score">6<b class="bar"></b></span><span class="score">3<b class="dots"></b></span><span class="score">7<b class="bar"></b></span><span class="score">7<b class="bar"></b></span><span class="buy"><svg><use href="#cart"/></svg>Buy Now</span></div>
  <div class="row"><span class="supplier">Bristle<br>Barrel</span><span class="name">Timberline</span><span><i class="bottle" role="img" aria-label="Beard oil bottle"></i></span><span>USA</span><span>Curabitur turpis</span><span>Cras mattis</span><span class="score">6<b class="bar"></b></span><span class="score">3<b class="dots"></b></span><span class="score">5<b class="bar"></b></span><span class="score">9<b class="bar"></b></span><span class="buy"><svg><use href="#cart"/></svg>Buy Now</span></div>
  <div class="row"><span class="supplier">Bristle<br>Barrel</span><span class="name">Timberline</span><span><i class="bottle" role="img" aria-label="Beard oil bottle"></i></span><span>USA</span><span>Curabitur turpis</span><span>Suspendisse<br>placerat</span><span class="score">6<b class="bar"></b></span><span class="score">3<b class="dots"></b></span><span class="score">7<b class="bar"></b></span><span class="score">7<b class="bar"></b></span><span class="buy"><svg><use href="#cart"/></svg>Buy Now</span></div>
  <div class="row"><span class="supplier">Bristle<br>Barrel</span><span class="name">Timberline</span><span><i class="bottle" role="img" aria-label="Beard oil bottle"></i></span><span>USA</span><span>Curabitur turpis</span><span>Cras mattis</span><span class="score">6<b class="bar"></b></span><span class="score">3<b class="dots"></b></span><span class="score">5<b class="bar"></b></span><span class="score">9<b class="bar"></b></span><span class="buy"><svg><use href="#cart"/></svg>Buy Now</span></div>
  <div class="row"><span class="supplier">Bristle<br>Barrel</span><span class="name">Timberline</span><span><i class="bottle" role="img" aria-label="Beard oil bottle"></i></span><span>USA</span><span>Curabitur turpis</span><span>Suspendisse<br>placerat</span><span class="score">6<b class="bar"></b></span><span class="score">3<b class="dots"></b></span><span class="score">7<b class="bar"></b></span><span class="score">7<b class="bar"></b></span><span class="buy"><svg><use href="#cart"/></svg>Buy Now</span></div>
  <div class="row"><span class="supplier">Bristle<br>Barrel</span><span class="name">Timberline</span><span><i class="bottle" role="img" aria-label="Beard oil bottle"></i></span><span>USA</span><span>Curabitur turpis</span><span>Cras mattis</span><span class="score">6<b class="bar"></b></span><span class="score">3<b class="dots"></b></span><span class="score">5<b class="bar"></b></span><span class="score">9<b class="bar"></b></span><span class="buy"><svg><use href="#cart"/></svg>Buy Now</span></div>
  <div class="row"><span class="supplier">Bristle<br>Barrel</span><span class="name">Timberline</span><span><i class="bottle" role="img" aria-label="Beard oil bottle"></i></span><span>USA</span><span>Curabitur turpis</span><span>Suspendisse<br>placerat</span><span class="score">6<b class="bar"></b></span><span class="score">3<b class="dots"></b></span><span class="score">7<b class="bar"></b></span><span class="score">7<b class="bar"></b></span><span class="buy"><svg><use href="#cart"/></svg>Buy Now</span></div>
</main>

<aside class="sidebar">
  <h2>Newsletter Subscribe</h2>
  <div class="subscribe"><span>Email Address</span><svg width="14" height="10" viewBox="0 0 14 10"><rect width="14" height="10" rx="1" fill="#fff"/><path d="M0 0l7 5 7-5" fill="none" stroke="#6b4a36" stroke-width="1.2"/></svg></div>
  <div class="social"><i></i><i></i><i></i><i></i><i></i><i></i><i></i></div>
  <div class="blog-title">Blog</div>
  <article class="post"><div class="thumb" role="img" aria-label="Blog photo of a bearded man" style="background:linear-gradient(160deg,#9a9a9a,#3e3e3e)"></div><div><p>Etiam consequat eta lacus felis viverra, eget rhoncus massa ullamcorper.</p><time>10 - Feb - 2016</time></div></article>
  <article class="post"><div class="thumb" role="img" aria-label="Blog photo of two bearded men" style="background:linear-gradient(160deg,#d8d4d0,#4a3b33)"></div><div><p>Etiam consequat eta lacus felis viverra, eget rhoncus massa ullamcorper.</p><time>10 - Feb - 2016</time></div></article>
  <article class="post"><div class="thumb" role="img" aria-label="Blog photo of a grey-bearded man" style="background:linear-gradient(160deg,#cfcfcf,#555)"></div><div><p>Etiam consequat eta lacus felis viverra, eget rhoncus massa ullamcorper.</p><time>10 - Feb - 2016</time></div></article>
  <article class="post"><div class="thumb" role="img" aria-label="Blog photo of barber tools on wood" style="background:linear-gradient(160deg,#7a4b33,#3a2418)"></div><div><p>Etiam consequat eta lacus felis viverra, eget rhoncus massa ullamcorper.</p><time>10 - Feb - 2016</time></div></article>
  <article class="post"><div class="thumb" role="img" aria-label="Blog photo of a red beard close-up" style="background:linear-gradient(160deg,#e8d8cc,#8a4a2a)"></div><div><p>Etiam consequat eta lacus felis viverra, eget rhoncus massa ullamcorper.</p><time>10 - Feb - 2016</time></div></article>
  <article class="post"><div class="thumb" role="img" aria-label="Blog photo of a bearded man" style="background:linear-gradient(160deg,#5a4a40,#1e1a18)"></div><div><p>Etiam consequat eta lacus felis viverra, eget rhoncus massa ullamcorper.</p><time>10 - Feb - 2016</time></div></article>
  <article class="post"><div class="thumb" role="img" aria-label="Blog photo of a bearded man in a hat" style="background:linear-gradient(160deg,#c9d2d8,#8a3a30)"></div><div><p>Etiam consequat eta lacus felis viverra, eget rhoncus massa ullamcorper.</p><time>10 - Feb - 2016</time></div></article>
  <article class="post"><div class="thumb" role="img" aria-label="Blog photo of a bearded man" style="background:linear-gradient(160deg,#e0e0e0,#2a2a2a)"></div><div><p>Etiam consequat eta lacus felis viverra, eget rhoncus massa ullamcorper.</p><time>10 - Feb - 2016</time></div></article>
  <article class="post"><div class="thumb" role="img" aria-label="Blog photo of a bearded man in a plaid shirt" style="background:linear-gradient(160deg,#bfb8b2,#8a2e2e)"></div><div><p>Etiam consequat eta lacus felis viverra, eget rhoncus massa ullamcorper.</p><time>10 - Feb - 2016</time></div></article>
  <article class="post"><div class="thumb" role="img" aria-label="Blog photo of a bearded man in glasses" style="background:linear-gradient(160deg,#e6e6e6,#4a3a32)"></div><div><p>Etiam consequat eta lacus felis viverra, eget rhoncus massa ullamcorper.</p><time>10 - Feb - 2016</time></div></article>
</aside>

<footer class="site-footer">
  <nav><span>Home</span><span>|</span><span>About Me</span><span>|</span><span>Beard Oil Review Methodology</span><span>|</span><span>Charter</span><span>|</span><span>Blog</span></nav>
  <p>Copyright © 2016 Top Whisker Tonic. All rights reserved. &nbsp; All rights reserved.</p>
</footer>
</body>
</html>
```